Three different companies capability statement

We are three companies looking to create one capability statement that combines all of our companies' capabilities into one 4-page brochure (for back and front printing). One company does not have one but we are providing all the companies' websites to be able to pull information from each. This capability statement is what will provide companies interested in working with us.
Company order: KTR, Bellmont, Brightwell
Please look through the pages of our sites:
This company does not have a capability statement yet to include Brightwell Partners, LLC. Please use this company’s contracted service and about me page, more than information about the tutoring services offered: https://brightwellstudyhub.example/
These two are attached in the brief
https://www.ktrsolutions.example/
https://bmxllcforward.example/

Please ask any questions you might have.
I created an example of information using ChatGPT and our websites. This does not need to be used. Just an example

Target Market(s)

Businesses who want to hire us

Industry/Entity Type

Contract work

Requirements
Must have
• All three companies logos, information for all three companies. NAICS codes. Some client partners. Certifications
Nice to have
• We like the one we uploaded that has 2- 4 pages
Should not have
• Pictures of owners

```html
<!DOCTYPE html>
<html lang="en">
<head>
<meta charset="utf-8">
<title>KTR · Bellmont · Brightwell — Capability Statement</title>
<link href="https://fonts.googleapis.com/css2?family=Poppins:ital,wght@0,400;0,500;0,600;0,700;0,800;1,600;1,700&family=Montserrat:wght@400;500;600&display=swap" rel="stylesheet">
<style>
:root{
  --stage:#888888;
  --navy:#1c1f66;
  --indigo:#3a2a9a;
  --purple:#4b2ea3;
  --violet:#5a33b3;
  --royal:#1f6fcc;
  --cyan:#17b2e6;
  --sky:#2aa7e8;
  --ink:#3b2d8f;
  --link:#1a62c0;
  --text:#4a4a4a;
  --paper:#f3f4f8;
  --orange:#f07a23;
  --charcoal:#3a3a3a;
  --white:#ffffff;
}
*{box-sizing:border-box;margin:0;padding:0}
html,body{width:1200px;height:839px;overflow:hidden}
body{background:var(--stage);font-family:"Poppins",sans-serif;position:relative}
.page-label{position:absolute;top:32px;width:120px;text-align:center;color:#f2f2f2;font-weight:700;font-size:14px;letter-spacing:.5px}
.page{position:absolute;top:50px;width:531px;height:750px;background:var(--paper);overflow:hidden}
.page--one{left:45px}
.page--two{left:617px}
.hero-bg{position:absolute;left:0;top:0;width:531px}
.abs{position:absolute}

/* titles */
.hero-title{position:absolute;left:0;width:531px;text-align:center;color:var(--white);font-weight:800;letter-spacing:.3px}
.page--one .hero-title{top:22px;font-size:25px}
.page--two .hero-title{top:14px;font-size:21px}

/* hexagons */
.hex{position:absolute;clip-path:polygon(50% 0,100% 25%,100% 75%,50% 100%,0 75%,0 25%)}
.hex__inner{position:absolute;inset:2px;clip-path:polygon(50% 0,100% 25%,100% 75%,50% 100%,0 75%,0 25%);display:flex;align-items:center;justify-content:center;text-align:center;color:var(--white);font-weight:700;line-height:1.12}
.hex--badge{width:82px;height:96px;background:#6fd6ff}
.hex--badge .hex__inner{background:linear-gradient(160deg,#2f78dc,#5a2fb2);font-size:10px;padding:0 6px}
.hex--cert{width:64px;height:72px;background:#4b78e0}
.hex--cert .hex__inner{background:linear-gradient(170deg,#22307c,#1b2263);font-size:6.3px;padding:0 5px}

/* intro */
.intro{position:absolute;left:30px;top:231px;width:471px;text-align:center;color:var(--white);font-weight:600;font-size:10.1px;line-height:12.7px}

/* logo strip */
.strip-frame{position:absolute;left:50px;top:355px;width:435px;height:88px;border:1.5px solid #3d3aa6;border-radius:10px;background:linear-gradient(180deg,#fff,#ececf1)}
.ribbon{position:absolute;height:22px;border-radius:11px;background:linear-gradient(90deg,#4a2ea0,#2aa4e8);color:var(--white);font-weight:700;display:flex;align-items:center;justify-content:center}
.ribbon--solutions{left:96px;top:344px;width:340px;font-size:13.5px}
.ribbon--past{left:166px;top:547px;width:200px;font-size:13px}
.dot{position:absolute;width:6px;height:6px;border-radius:50%;background:var(--indigo)}
.wordmark{position:absolute;top:390px;display:flex;align-items:center;gap:5px;font-family:"Poppins",sans-serif;font-weight:600;font-size:15px;color:#24418f}
.wordmark__mark{width:18px;height:18px;border-radius:50%;background:#24418f}

/* strengths */
.strengths-title{position:absolute;left:40px;top:518px;font-size:15px;font-weight:700;color:var(--ink);line-height:18px}
.strength{position:absolute;width:360px}
.strength h3{font-size:10.3px;font-weight:700;color:var(--link);line-height:13px}
.strength p{font-family:"Montserrat",sans-serif;font-size:8.3px;color:var(--text);line-height:10.5px;margin-top:1px}

/* naics */
.naics-tab{position:absolute;left:33px;top:632px;width:120px;height:22px;background:var(--orange);border-radius:10px 10px 0 0;color:var(--white);font-weight:700;font-size:13px;padding:3px 0 0 17px}
.naics-box{position:absolute;left:33px;top:650px;width:474px;height:60px;background:var(--orange);border-radius:0 12px 12px 12px;display:grid;grid-template-columns:repeat(7,60px);column-gap:4.5px;row-gap:4px;padding:8px 0 0 14px}
.code{height:12px;border:1px solid #fff;border-radius:3px;color:var(--white);font-size:7.3px;font-weight:600;display:flex;align-items:center;gap:3px;padding-left:2px}
.code svg{flex:none}

/* footer */
.footer{position:absolute;left:0;top:720px;width:531px;height:30px;background:linear-gradient(90deg,#4b2c9e,#3f4fb8 55%,#29a8e8);color:var(--white);font-size:10px;display:flex;align-items:center}
.footer__item{position:absolute;display:flex;align-items:center;gap:4px}
.footer__rule{position:absolute;top:7px;width:1px;height:16px;background:rgba(255,255,255,.5)}

/* service cards */
.card{position:absolute;top:223px;width:155px;height:265px;border-radius:10px;overflow:hidden;color:var(--white);text-align:center}
.card--edu{left:27px;background:var(--purple)}
.card--fac{left:192px;background:var(--royal)}
.card--con{left:356px;background:var(--violet)}
.card__head{height:28px;background:#2a2577;font-size:7px;font-weight:700;line-height:8.3px;display:flex;align-items:center;justify-content:center;padding:0 8px}
.card--fac .card__head{background:#1f3f95}
.card__sub{font-size:7px;font-weight:700;line-height:8.2px;margin:7px 8px 0}
.card__body{font-family:"Montserrat",sans-serif;font-size:7.9px;line-height:9.6px;margin:6px 8px 0;color:#e3e4ff}
.card__list{list-style:none;text-align:left;margin:7px 10px 0 16px;font-size:7.1px;line-height:8.4px}
.card__list li{position:relative;padding-left:9px}
.card__list li::before{content:"";position:absolute;left:0;top:2px;border-left:4px solid #fff;border-top:2.5px solid transparent;border-bottom:2.5px solid transparent}
.card__list--spaced li{margin-bottom:6px}
.card__tail{font-family:"Montserrat",sans-serif;font-size:7.3px;line-height:8.6px;margin:6px 10px 0;color:#e3e4ff}

.tagline{position:absolute;left:30px;top:501px;width:471px;text-align:center;font-size:9.2px;font-weight:700;font-style:italic;color:var(--ink);line-height:10.9px}
.past-frame{position:absolute;left:27px;top:558px;width:483px;height:88px;border:1.5px solid #3d3aa6;border-radius:10px;background:#fff}
.badge-row{position:absolute;left:40px;width:458px;display:flex;align-items:center;justify-content:space-between}
.badge{background:#c9cfdc;border-radius:3px}
.badge--round{border-radius:50%}
.cta-question{position:absolute;left:0;top:665px;width:531px;text-align:center;font-size:12.3px;font-weight:700;color:var(--ink)}
.cta-pill{position:absolute;left:98px;top:692px;width:320px;height:30px;background:var(--charcoal);border-radius:14px 14px 0 0;color:var(--white);font-size:15px;font-weight:600;display:flex;align-items:center;justify-content:center}
</style>
</head>
<body>

<div class="page-label" style="left:247px">PAGE 1</div>
<div class="page-label" style="left:806px">PAGE 2</div>

<!-- ================= PAGE 1 ================= -->
<section class="page page--one">
  <svg class="hero-bg" width="531" height="336" viewBox="0 0 531 336" role="img" aria-label="Deep blue banner with faint network-line texture">
    <defs>
      <linearGradient id="p1Blue" x1="0" y1="0" x2="1" y2="0"><stop offset="0" stop-color="#1a57b8"/><stop offset="1" stop-color="#00b6e6"/></linearGradient>
      <linearGradient id="p1Navy" x1="0" y1="0" x2="1" y2="1"><stop offset="0" stop-color="#1b2a78"/><stop offset=".6" stop-color="#2f2a8f"/><stop offset="1" stop-color="#3d2a9c"/></linearGradient>
    </defs>
    <rect width="531" height="336" fill="url(#p1Blue)"/>
    <polygon points="0,140 531,134 531,175 266,222 0,170" fill="#33c6f0" opacity=".55"/>
    <polygon points="0,0 531,0 531,143 266,219 0,149" fill="url(#p1Navy)"/>
    <polyline points="0,150 266,220 531,143" fill="none" stroke="#fff" stroke-width="2"/>
  </svg>
  <h1 class="hero-title">UNIFIED VISION FOR EXCELLENCE</h1>

  <div class="hex hex--badge" style="left:86px;top:69px"><div class="hex__inner">SERVICE DISABLED VETERAN OWNED</div></div>
  <div class="hex hex--badge" style="left:177px;top:69px"><div class="hex__inner">WOMAN OWNED</div></div>
  <div class="hex hex--badge" style="left:268px;top:69px"><div class="hex__inner">MINORITY OWNED</div></div>
  <div class="hex hex--badge" style="left:359px;top:69px"><div class="hex__inner">HUB ZONED</div></div>

  <p class="intro">In response to today's demand for flexible solutions, we've united Service-Disabled Veteran Owned, Woman-Owned, Minority-Owned, and Hub-zone certified companies in a unique partnership. Brightwell Partners, LLC, KTR Facility Services, LLC, and Bellmont Consulting Group, LLC come together to offer a blend of educational innovation, facility management, and strategic consulting. This collaboration is dedicated to addressing complex challenges efficiently across all sectors and levels, driving swift advancements in service delivery and innovation.</p>

  <div class="strip-frame"></div>
  <span class="dot" style="left:88px;top:352px"></span>
  <span class="dot" style="left:443px;top:352px"></span>
  <div class="ribbon ribbon--solutions">Unified Solutions for Tomorrow’s Challenges</div>
  <div class="wordmark" style="left:98px"><span class="wordmark__mark"></span>Brightwell</div>
  <div class="wordmark" style="left:200px"><span class="wordmark__mark"></span>KTR</div>
  <div class="wordmark" style="left:290px"><span class="wordmark__mark"></span>Bellmont</div>

  <svg class="abs" style="left:0;top:455px" width="180" height="160" viewBox="0 0 180 160">
    <path d="M54 4 Q 135 20 135 77 Q 135 134 54 150" fill="none" stroke="var(--orange)" stroke-width="2"/>
    <g fill="#fff" stroke="var(--orange)" stroke-width="3">
      <circle cx="106" cy="19" r="5.5"/><circle cx="134" cy="77" r="5.5"/><circle cx="106" cy="138" r="5.5"/>
    </g>
    <g stroke="var(--orange)" stroke-width="1" stroke-dasharray="2 2">
      <line x1="113" y1="19" x2="135" y2="19"/><line x1="141" y1="77" x2="160" y2="77"/><line x1="113" y1="138" x2="135" y2="138"/>
    </g>
  </svg>
  <div class="strengths-title">Combined<br>Strengths</div>

  <div class="strength" style="left:142px;top:467px">
    <h3>Brightwell Partners, LLC,</h3>
    <p>delivers expert educational consulting and curriculum development, driving advancements in teaching strategies and student performance with innovative, tailored solutions.</p>
  </div>
  <div class="strength" style="left:165px;top:525px">
    <h3>KTR Facility Services, LLC,</h3>
    <p>optimizes facility efficiency and asset longevity through advanced technology, best practices, and a dedicated team, providing cost-effective, tailored solutions for various clients.</p>
  </div>
  <div class="strength" style="left:142px;top:580px">
    <h3>Bellmont Consulting Group, LLC,</h3>
    <p>offers innovative consulting and strategic solutions, driving businesses ahead with advanced insights and actionable strategies to secure measurable growth and a competitive edge in the market.</p>
  </div>

  <div class="naics-tab">NAICS Codes</div>
  <div class="naics-box">
    <span class="code"><svg width="8" height="8" viewBox="0 0 8 8"><circle cx="4" cy="4" r="3.4" fill="none" stroke="#fff" stroke-width=".9"/><path d="M2.3 4 3.6 5.2 5.8 2.8" fill="none" stroke="#fff" stroke-width=".9"/></svg>541930</span>
    <span class="code"><svg width="8" height="8" viewBox="0 0 8 8"><circle cx="4" cy="4" r="3.4" fill="none" stroke="#fff" stroke-width=".9"/><path d="M2.3 4 3.6 5.2 5.8 2.8" fill="none" stroke="#fff" stroke-width=".9"/></svg>611513</span>
    <span class="code"><svg width="8" height="8" viewBox="0 0 8 8"><circle cx="4" cy="4" r="3.4" fill="none" stroke="#fff" stroke-width=".9"/><path d="M2.3 4 3.6 5.2 5.8 2.8" fill="none" stroke="#fff" stroke-width=".9"/></svg>541611</span>
    <span class="code"><svg width="8" height="8" viewBox="0 0 8 8"><circle cx="4" cy="4" r="3.4" fill="none" stroke="#fff" stroke-width=".9"/><path d="M2.3 4 3.6 5.2 5.8 2.8" fill="none" stroke="#fff" stroke-width=".9"/></svg>541612</span>
    <span class="code"><svg width="8" height="8" viewBox="0 0 8 8"><circle cx="4" cy="4" r="3.4" fill="none" stroke="#fff" stroke-width=".9"/><path d="M2.3 4 3.6 5.2 5.8 2.8" fill="none" stroke="#fff" stroke-width=".9"/></svg>541618</span>
    <span class="code"><svg width="8" height="8" viewBox="0 0 8 8"><circle cx="4" cy="4" r="3.4" fill="none" stroke="#fff" stroke-width=".9"/><path d="M2.3 4 3.6 5.2 5.8 2.8" fill="none" stroke="#fff" stroke-width=".9"/></svg>611430</span>
    <span class="code"><svg width="8" height="8" viewBox="0 0 8 8"><circle cx="4" cy="4" r="3.4" fill="none" stroke="#fff" stroke-width=".9"/><path d="M2.3 4 3.6 5.2 5.8 2.8" fill="none" stroke="#fff" stroke-width=".9"/></svg>541613</span>
    <span class="code"><svg width="8" height="8" viewBox="0 0 8 8"><circle cx="4" cy="4" r="3.4" fill="none" stroke="#fff" stroke-width=".9"/><path d="M2.3 4 3.6 5.2 5.8 2.8" fill="none" stroke="#fff" stroke-width=".9"/></svg>611710</span>
    <span class="code"><svg width="8" height="8" viewBox="0 0 8 8"><circle cx="4" cy="4" r="3.4" fill="none" stroke="#fff" stroke-width=".9"/><path d="M2.3 4 3.6 5.2 5.8 2.8" fill="none" stroke="#fff" stroke-width=".9"/></svg>611691</span>
    <span class="code"><svg width="8" height="8" viewBox="0 0 8 8"><circle cx="4" cy="4" r="3.4" fill="none" stroke="#fff" stroke-width=".9"/><path d="M2.3 4 3.6 5.2 5.8 2.8" fill="none" stroke="#fff" stroke-width=".9"/></svg>541820</span>
    <span class="code"><svg width="8" height="8" viewBox="0 0 8 8"><circle cx="4" cy="4" r="3.4" fill="none" stroke="#fff" stroke-width=".9"/><path d="M2.3 4 3.6 5.2 5.8 2.8" fill="none" stroke="#fff" stroke-width=".9"/></svg>56131</span>
    <span class="code"><svg width="8" height="8" viewBox="0 0 8 8"><circle cx="4" cy="4" r="3.4" fill="none" stroke="#fff" stroke-width=".9"/><path d="M2.3 4 3.6 5.2 5.8 2.8" fill="none" stroke="#fff" stroke-width=".9"/></svg>5512110</span>
    <span class="code"><svg width="8" height="8" viewBox="0 0 8 8"><circle cx="4" cy="4" r="3.4" fill="none" stroke="#fff" stroke-width=".9"/><path d="M2.3 4 3.6 5.2 5.8 2.8" fill="none" stroke="#fff" stroke-width=".9"/></svg>611519</span>
    <span class="code"><svg width="8" height="8" viewBox="0 0 8 8"><circle cx="4" cy="4" r="3.4" fill="none" stroke="#fff" stroke-width=".9"/><path d="M2.3 4 3.6 5.2 5.8 2.8" fill="none" stroke="#fff" stroke-width=".9"/></svg>561210</span>
    <span class="code"><svg width="8" height="8" viewBox="0 0 8 8"><circle cx="4" cy="4" r="3.4" fill="none" stroke="#fff" stroke-width=".9"/><path d="M2.3 4 3.6 5.2 5.8 2.8" fill="none" stroke="#fff" stroke-width=".9"/></svg>561422</span>
    <span class="code"><svg width="8" height="8" viewBox="0 0 8 8"><circle cx="4" cy="4" r="3.4" fill="none" stroke="#fff" stroke-width=".9"/><path d="M2.3 4 3.6 5.2 5.8 2.8" fill="none" stroke="#fff" stroke-width=".9"/></svg>561320</span>
    <span class="code"><svg width="8" height="8" viewBox="0 0 8 8"><circle cx="4" cy="4" r="3.4" fill="none" stroke="#fff" stroke-width=".9"/><path d="M2.3 4 3.6 5.2 5.8 2.8" fill="none" stroke="#fff" stroke-width=".9"/></svg>221320</span>
    <span class="code"><svg width="8" height="8" viewBox="0 0 8 8"><circle cx="4" cy="4" r="3.4" fill="none" stroke="#fff" stroke-width=".9"/><path d="M2.3 4 3.6 5.2 5.8 2.8" fill="none" stroke="#fff" stroke-width=".9"/></svg>561110</span>
    <span class="code"><svg width="8" height="8" viewBox="0 0 8 8"><circle cx="4" cy="4" r="3.4" fill="none" stroke="#fff" stroke-width=".9"/><path d="M2.3 4 3.6 5.2 5.8 2.8" fill="none" stroke="#fff" stroke-width=".9"/></svg>561720</span>
    <span class="code"><svg width="8" height="8" viewBox="0 0 8 8"><circle cx="4" cy="4" r="3.4" fill="none" stroke="#fff" stroke-width=".9"/><path d="M2.3 4 3.6 5.2 5.8 2.8" fill="none" stroke="#fff" stroke-width=".9"/></svg>561499</span>
    <span class="code"><svg width="8" height="8" viewBox="0 0 8 8"><circle cx="4" cy="4" r="3.4" fill="none" stroke="#fff" stroke-width=".9"/><path d="M2.3 4 3.6 5.2 5.8 2.8" fill="none" stroke="#fff" stroke-width=".9"/></svg>561990</span>
  </div>

  <footer class="footer">
    <span class="footer__item" style="left:33px"><svg width="11" height="11" viewBox="0 0 24 24" fill="none" stroke="#fff" stroke-width="2"><path d="M22 16.9v3a2 2 0 0 1-2.2 2 19.8 19.8 0 0 1-8.6-3.1 19.5 19.5 0 0 1-6-6A19.8 19.8 0 0 1 2.1 4.2 2 2 0 0 1 4.1 2h3a2 2 0 0 1 2 1.7c.1.9.4 1.8.7 2.7a2 2 0 0 1-.5 2.1L8 9.8a16 16 0 0 0 6 6l1.3-1.3a2 2 0 0 1 2.1-.4c.9.3 1.8.6 2.7.7a2 2 0 0 1 1.7 2z"/></svg>404-555-0187</span>
    <span class="footer__rule" style="left:143px"></span>
    <span class="footer__item" style="left:168px"><svg width="12" height="10" viewBox="0 0 24 18" fill="none" stroke="#fff" stroke-width="2"><rect x="1" y="1" width="22" height="16"/><path d="M1 1l11 9 11-9"/></svg>contactus@ktrsolutions.example</span>
    <span class="footer__rule" style="left:350px"></span>
    <span class="footer__item" style="left:372px"><svg width="11" height="11" viewBox="0 0 24 24" fill="none" stroke="#fff" stroke-width="2"><circle cx="12" cy="12" r="10"/><path d="M2 12h20M12 2a15 15 0 0 1 0 20M12 2a15 15 0 0 0 0 20"/></svg>www.ktrsolutions.example</span>
  </footer>
</section>

<!-- ================= PAGE 2 ================= -->
<section class="page page--two">
  <svg class="hero-bg" width="531" height="240" viewBox="0 0 531 240" role="img" aria-label="Deep blue banner with faint network-line texture">
    <defs>
      <linearGradient id="p2Navy" x1="0" y1="0" x2="1" y2="1"><stop offset="0" stop-color="#1b2a78"/><stop offset=".6" stop-color="#2c2a8c"/><stop offset="1" stop-color="#3d2a9c"/></linearGradient>
    </defs>
    <polygon points="0,195 531,188 531,206 266,232 0,215" fill="#2aa7e8"/>
    <polygon points="0,0 531,0 531,190 266,224 0,197" fill="url(#p2Navy)"/>
    <polyline points="0,197 266,224 531,190" fill="none" stroke="#fff" stroke-width="1.5"/>
  </svg>
  <h1 class="hero-title">CERTIFICATIONS AND LICENSES</h1>

  <div class="hex hex--cert" style="left:35px;top:50px"><div class="hex__inner">CCR &amp; OCRA Compliant (SAMS)</div></div>
  <div class="hex hex--cert" style="left:111px;top:50px"><div class="hex__inner">Harlow County Minority Business Enterprise (MBE)</div></div>
  <div class="hex hex--cert" style="left:188px;top:50px"><div class="hex__inner">Ridgeford County Water Authority (SLBE)</div></div>
  <div class="hex hex--cert" style="left:265px;top:50px"><div class="hex__inner">Small Business</div></div>
  <div class="hex hex--cert" style="left:344px;top:50px"><div class="hex__inner">Service Disabled Veteran Owned Business (SDVOB)</div></div>
  <div class="hex hex--cert" style="left:425px;top:50px"><div class="hex__inner">Ridgeford County Minority Business Enterprise (MBE)</div></div>

  <div class="hex hex--cert" style="left:35px;top:128px"><div class="hex__inner">Small Disadvantage Business (SDB)</div></div>
  <div class="hex hex--cert" style="left:111px;top:128px"><div class="hex__inner">NR-DOT Disadvantage Business Enterprise (DBE)</div></div>
  <div class="hex hex--cert" style="left:188px;top:128px"><div class="hex__inner">Ridgeford County Small Local Business Enterprise (SLBE)</div></div>
  <div class="hex hex--cert" style="left:265px;top:128px"><div class="hex__inner">RMSDC - MBE</div></div>
  <div class="hex hex--cert" style="left:344px;top:128px"><div class="hex__inner">Minority Business</div></div>
  <div class="hex hex--cert" style="left:425px;top:128px"><div class="hex__inner">SR-DOT Disadvantage Business Enterprise (DBE)</div></div>

  <article class="card card--edu">
    <h2 class="card__head">Education and Professional Development</h2>
    <h3 class="card__sub">Empowering Education through Innovation and Expertise</h3>
    <p class="card__body">At the intersection of pioneering education and professional growth lies our unique coalition. We leverage Brightwell Partners, LLC's educational excellence and unparalleled learning experiences.</p>
    <ul class="card__list card__list--spaced">
      <li>Custom curriculum development focusing on inclusivity and engagement</li>
      <li>Leadership training programs for emerging and established leaders</li>
      <li>Professional development workshops designed to enhance skills across various industries.</li>
    </ul>
    <p class="card__tail">to enhance learning engagement and outcomes through tailored, cost-effective, and accessible learning solutions.</p>
  </article>

  <article class="card card--fac">
    <h2 class="card__head">Facility Management and Support</h2>
    <h3 class="card__sub">Streamlining Operations with Premier Facility Solutions</h3>
    <p class="card__body">KTR Facility Services, LLC, renowned for its commitment to enhancing workplace performance, delivers a comprehensive suite of services tailored to meet the evolving needs of our diverse clientele.</p>
    <ul class="card__list">
      <li>Asset Tracking</li>
      <li>Staff Recruitment &amp; Training</li>
      <li>Computerized Management Systems</li>
      <li>Preventive, Corrective, &amp; Predictive Maintenance</li>
      <li>Facility Custodial Services utilizing advanced technology</li>
    </ul>
    <p class="card__tail" style="margin-top:12px">best practices, and a dedicated team ensures efficient and effective facility management, enhancing competitive edge in the global marketplace.</p>
  </article>

  <article class="card card--con">
    <h2 class="card__head">Innovative Consulting and Strategic Solutions</h2>
    <h3 class="card__sub">Advancing Business Goals with Strategic Insight</h3>
    <p class="card__body">Harnessing Bellmont Consulting Group, LLC's strategic acumen and the collective expertise of our partners and expansive network, we deliver bespoke consulting services tailored to navigate today's complex business ecosystems.</p>
    <ul class="card__list">
      <li>Community Integration and Key Partnership Development</li>
      <li>Translation Services</li>
      <li>Marketing, Brand strategy development</li>
      <li>Change Management</li>
      <li>Performance and Improvement Strategies</li>
      <li>Research and Analysis</li>
    </ul>
    <p class="card__tail">custom solutions for tech, healthcare, energy, and education sectors, emphasizing the group's ability to adapt and respond to specific industry challenges.</p>
  </article>

  <p class="tagline">Our collective expertise across these core areas ensures that no matter your challenge, we have the tailored solution to propel your organization forward. With our integrated approach, we're not just service providers; we're your partners in success.</p>

  <div class="past-frame"></div>
  <span class="dot" style="left:155px;top:555px"></span>
  <span class="dot" style="left:370px;top:555px"></span>
  <div class="ribbon ribbon--past">Past Performance</div>

  <div class="badge-row" style="top:583px">
    <span class="badge" style="width:48px;height:20px"></span>
    <span class="badge" style="width:44px;height:16px;background:#8fc3ea"></span>
    <span class="badge badge--round" style="width:14px;height:14px;background:#9fb7dc"></span>
    <span class="badge" style="width:50px;height:16px;background:#b7c3e0"></span>
    <span class="badge badge--round" style="width:22px;height:22px;background:#b9bfd4"></span>
    <span class="badge badge--round" style="width:22px;height:22px;background:#aab6d6"></span>
    <span class="badge badge--round" style="width:22px;height:22px;background:#9fb1cf"></span>
    <span class="badge" style="width:88px;height:8px;background:#a9bde6"></span>
    <span class="badge badge--round" style="width:22px;height:22px;background:#e3c77a"></span>
    <span class="badge badge--round" style="width:22px;height:22px;background:#c4c4c4"></span>
    <span class="badge" style="width:22px;height:30px;background:#a7b2d2"></span>
  </div>
  <div class="badge-row" style="top:614px">
    <span class="badge" style="width:52px;height:20px;background:#d2d2d2"></span>
    <span class="badge badge--round" style="width:20px;height:20px;background:#e3c4c4"></span>
    <span class="badge" style="width:48px;height:12px;background:#d9b0b0"></span>
    <span class="badge badge--round" style="width:22px;height:22px;background:#a9afc9"></span>
    <span class="badge" style="width:54px;height:14px"></span>
    <span class="badge badge--round" style="width:22px;height:22px;background:#c8c8c8"></span>
    <span class="badge" style="width:66px;height:10px"></span>
    <span class="badge badge--round" style="width:22px;height:22px;background:#aab6d6"></span>
    <span class="badge" style="width:44px;height:16px;background:#b7c3e0"></span>
    <span class="badge" style="width:36px;height:14px;background:#9fb1e0"></span>
  </div>

  <p class="cta-question">Ready to explore how our services can transform your organization?</p>
  <div class="cta-pill">Contact us to start the conversation</div>

  <footer class="footer">
    <span class="footer__item" style="left:38px"><svg width="11" height="11" viewBox="0 0 24 24" fill="none" stroke="#fff" stroke-width="2"><path d="M22 16.9v3a2 2 0 0 1-2.2 2 19.8 19.8 0 0 1-8.6-3.1 19.5 19.5 0 0 1-6-6A19.8 19.8 0 0 1 2.1 4.2 2 2 0 0 1 4.1 2h3a2 2 0 0 1 2 1.7c.1.9.4 1.8.7 2.7a2 2 0 0 1-.5 2.1L8 9.8a16 16 0 0 0 6 6l1.3-1.3a2 2 0 0 1 2.1-.4c.9.3 1.8.6 2.7.7a2 2 0 0 1 1.7 2z"/></svg>404-555-0187</span>
    <span class="footer__rule" style="left:148px"></span>
    <span class="footer__item" style="left:172px"><svg width="12" height="10" viewBox="0 0 24 18" fill="none" stroke="#fff" stroke-width="2"><rect x="1" y="1" width="22" height="16"/><path d="M1 1l11 9 11-9"/></svg>contactus@ktrsolutions.example</span>
    <span class="footer__rule" style="left:355px"></span>
    <span class="footer__item" style="left:376px"><svg width="11" height="11" viewBox="0 0 24 24" fill="none" stroke="#fff" stroke-width="2"><circle cx="12" cy="12" r="10"/><path d="M2 12h20M12 2a15 15 0 0 1 0 20M12 2a15 15 0 0 0 0 20"/></svg>www.ktrsolutions.example</span>
  </footer>
</section>

</body>
</html>
```